Powerpoint template for Trivia Company

Revamp of our current powerpoint template to make it more professional and fun for the players. Something worthy of a trivia company. Please see logo attached for potential colour - but also open to other ideas.

NO BRANDING REQUIRED (IE: No mention of our company or logo on the template please)

Target Market(s)

Bars/restaurants

Colors
3176b5
00a990

```html
<!DOCTYPE html>
<html lang="en">
<head>
<meta charset="utf-8">
<title>Welcome to Trivia Night</title>
<link rel="stylesheet" href="https://fonts.googleapis.com/css2?family=Source+Sans+3:wght@900&display=swap">
<style>
  :root {
    --brand-blue: #3176b5;
    --brand-teal: #00a990;
    --brand-lime: #adc524;
    --ink: #000000;
    --paper: #ffffff;
  }
  html, body {
    margin: 0;
    padding: 0;
    overflow: hidden;
    background: var(--paper);
  }
  .slide {
    position: relative;
    width: 1200px;
    height: 1000px;
    background: var(--paper);
    overflow: hidden;
  }
  .corner-accent {
    position: absolute;
  }
  .corner-accent--top-left {
    left: 0; top: 0; width: 345px; height: 318px;
    background: radial-gradient(ellipse at 0 0,
      var(--brand-blue) 0%, var(--brand-teal) 40%, var(--brand-lime) 62%, rgba(255,255,255,0) 100%);
  }
  .corner-accent--top-right {
    right: 0; top: 0; width: 235px; height: 217px;
    background: radial-gradient(ellipse at 100% 0,
      var(--brand-blue) 0%, var(--brand-teal) 40%, var(--brand-lime) 62%, rgba(255,255,255,0) 100%);
  }
  .corner-accent--bottom-left {
    left: 0; bottom: 0; width: 237px; height: 220px;
    background: radial-gradient(ellipse at 0 100%,
      var(--brand-blue) 0%, var(--brand-teal) 40%, var(--brand-lime) 62%, rgba(255,255,255,0) 100%);
  }
  .corner-accent--bottom-right {
    right: 0; bottom: 0; width: 345px; height: 318px;
    background: radial-gradient(ellipse at 100% 100%,
      var(--brand-blue) 0%, var(--brand-teal) 40%, var(--brand-lime) 62%, rgba(255,255,255,0) 100%);
  }
  .slide-title {
    position: absolute;
    left: 0;
    right: 0;
    top: 288px;
    margin: 0;
    text-align: center;
    font-family: "Source Sans 3", "Myriad Pro", Arial, sans-serif;
    font-weight: 900;
    font-size: 148px;
    line-height: 172px;
    letter-spacing: 0;
    color: var(--ink);
    text-transform: uppercase;
  }
  .slide-title .line { display: block; white-space: nowrap; }
</style>
</head>
<body>
<main class="slide">
  <div class="corner-accent corner-accent--top-left" role="img" aria-label="Swirling ribbon ornament in blue, teal and lime green"></div>
  <div class="corner-accent corner-accent--top-right" role="img" aria-label="Swirling ribbon ornament in blue, teal and lime green"></div>
  <div class="corner-accent corner-accent--bottom-left" role="img" aria-label="Swirling ribbon ornament in blue, teal and lime green"></div>
  <div class="corner-accent corner-accent--bottom-right" role="img" aria-label="Swirling ribbon ornament in blue, teal and lime green"></div>

  <h1 class="slide-title">
    <span class="line">Wel Come To</span>
    <span class="line">Trivia Night</span>
  </h1>
</main>
</body>
</html>
```